Single Page website for Product Company

I need a website designed for my small startup company "Lantern Yard Furnishings". We design and manufacture custom innovative indoor/outdoor entertainment furnishings e.g. outdoor TV enclosures, outdoor bars and outdoor kitchens. I'm looking for a single page site based on the the tinyShelf-SoloView-storefront bootstrap page, attached.

I've also attached pictures of my products, these need to be photoshopped and placed in an outdoor patio area if possible.

Target Market(s)

Home owners

Industry/Entity Type

It Company

Coding

Coded - Design and coding required

Number of Pages Required

1 page

Requirements
Must have
• Must be single page site built with attached bootstrap template and adjust to screen size e.g. ipad, mobile phone and computer
Nice to have
• Integration with vendaro

```html
<!DOCTYPE html>
<html lang="en">
<head>
<meta charset="utf-8">
<title>Lantern Yard Furnishings</title>
<link rel="stylesheet" href="https://fonts.googleapis.com/css2?family=Open+Sans:wght@400;600;700&display=swap">
<style>
:root{
  --orange:#f39322;
  --ink:#222629;
  --text:#555b61;
  --muted:#9aa0a6;
  --line:#e3e5e8;
  --band:#f1f1f1;
  --slate:#2f3640;
  --sky:#3cb6de;
  --foot:#3a3d42;
  --white:#ffffff;
}
*{box-sizing:border-box;margin:0;padding:0}
html,body{width:1200px;height:4082px;overflow:hidden}
body{font-family:"Open Sans",Arial,sans-serif;color:var(--text);background:var(--white);position:relative}
section,header,footer{position:absolute;left:0;width:1200px}
.abs{position:absolute}
.btn{position:absolute;background:var(--orange);color:var(--white);font-weight:700;font-size:13px;letter-spacing:.5px;display:flex;align-items:center;justify-content:center;text-transform:uppercase}
.btn-outline{background:transparent;border:2px solid var(--orange);color:var(--orange)}
.field{position:absolute;height:41px;border:1px solid #dadde0;background:var(--white);font-size:13px;color:var(--muted);padding:0 14px;display:flex;align-items:center}
.field.select::after{content:"⌄";position:absolute;right:14px;top:8px;font-size:14px;color:#999}
.section-title{position:absolute;left:0;width:1200px;text-align:center;font-weight:700;font-size:21px;color:var(--ink);letter-spacing:.5px}
.label{position:absolute;font-size:13px;font-weight:700;color:var(--ink);text-transform:uppercase}

/* hero */
.hero{top:0;height:637px;background:linear-gradient(180deg,#3a3530 0%,#2a2622 40%,#4a3b30 70%,#2d2622 100%)}
.hero-shade{position:absolute;inset:0;background:rgba(0,0,0,.25)}
.brand{position:absolute;left:96px;top:42px;display:flex;align-items:center;gap:10px;color:#6fb3e6;font-size:26px;font-weight:600}
.brand-mark{width:22px;height:22px;background:var(--orange)}
.nav{position:absolute;top:52px;right:96px;display:flex;gap:56px;font-size:12px;font-weight:600;color:var(--white);text-transform:uppercase}
.hero-title{position:absolute;top:262px;width:1200px;text-align:center;color:var(--white);font-size:26px;font-weight:700;letter-spacing:.5px}
.hero-text{position:absolute;top:312px;left:270px;width:660px;text-align:center;color:var(--white);font-size:15px;line-height:28px}
.dots{position:absolute;display:flex;gap:7px}
.dots i{width:7px;height:7px;border-radius:50%;background:rgba(255,255,255,.5)}
.dots i.on{background:var(--orange)}

/* products */
.products{top:637px;height:457px}
.product{position:absolute;top:133px;width:302px}
.product-photo{height:201px;background:linear-gradient(180deg,#8e8578 0%,#3d3a3a 45%,#a88b6c 80%,#6b5a4a 100%)}
.product-meta{display:flex;justify-content:space-between;margin-top:18px;font-size:12px;font-weight:700;color:var(--ink);text-transform:uppercase}
.product-meta b{font-size:15px}

/* shipping */
.shipping{top:1094px;height:146px;background:var(--band)}
.shipping-text{position:absolute;left:98px;top:56px;font-size:21px;color:var(--ink)}

/* about */
.about{top:1240px;height:324px}
.about-title{position:absolute;left:108px;top:100px;font-size:21px;font-weight:700;color:var(--ink);text-transform:uppercase}
.about-sub{position:absolute;left:108px;top:136px;font-size:16px;color:var(--ink)}
.about-text{position:absolute;left:449px;top:92px;width:640px;font-size:13px;line-height:28px;color:var(--muted)}

/* testimonial */
.testimonial{top:1564px;height:367px;background:linear-gradient(180deg,#2d2a27 0%,#2b2a2c 45%,#4a3b30 75%,#2a2420 100%)}
.quote{position:absolute;top:108px;width:1200px;text-align:center;color:var(--white);font-size:22px;line-height:38px}
.quote-name{position:absolute;top:206px;width:1200px;text-align:center;color:var(--orange);font-size:15px}

/* newsletter */
.newsletter{top:1931px;height:294px;background:var(--slate)}
.newsletter h2{position:absolute;top:72px;width:1200px;text-align:center;color:var(--white);font-size:21px;font-weight:700}
.newsletter p{position:absolute;top:110px;width:1200px;text-align:center;color:#dfe3e8;font-size:16px}

/* order */
.order{top:2225px;height:990px}
.table-row{position:absolute;left:98px;width:1001px;height:60px;border-bottom:1px solid var(--line);font-size:13px;color:var(--ink)}
.table-row span{position:absolute;top:22px}
.table-head span{font-weight:700;font-size:12px;text-transform:uppercase}
.table-row em{font-style:normal;color:var(--muted)}
.qty{position:absolute;left:626px;top:12px;width:70px;height:34px;border:1px solid #dadde0;font-size:12px;padding:9px 10px;color:var(--text)}
.summary-row{position:absolute;left:620px;width:479px;font-size:13px;display:flex;justify-content:space-between;color:var(--text)}

/* features */
.features{top:3215px;height:248px;background:var(--sky)}
.feature{position:absolute;top:66px;width:260px;text-align:center;color:var(--white);font-size:15px;font-weight:700}
.feature svg{display:block;margin:0 auto 28px}

/* contact */
.contact{top:3463px;height:517px}
.contact-sub{position:absolute;top:118px;width:1200px;text-align:center;font-size:14px;color:var(--muted)}
.contact-info{position:absolute;left:207px;top:190px;font-size:12px;line-height:22px;color:var(--muted)}
.contact-info strong{display:block;color:var(--ink);font-size:13px;margin-bottom:12px}
.contact-info .line{display:flex;align-items:center;gap:8px}

/* footer */
.footer{top:3980px;height:102px;background:var(--foot);color:#c5c9ce;font-size:12px}
.social{position:absolute;right:112px;top:36px;display:flex;gap:10px}
.social i{width:28px;height:28px;border-radius:50%;background:#c5c9ce}
</style>
</head>
<body>

<header class="hero">
  <div class="abs" style="inset:0" role="img" aria-label="Photo of two televisions mounted above a stone entertainment cabinet with glowing blue speakers"></div>
  <div class="hero-shade"></div>
  <div class="brand"><span class="brand-mark"></span>Lantern Yard Furnishings</div>
  <nav class="nav"><span>Products</span><span>About</span><span>Order</span><span>Contact</span><span>External link</span></nav>
  <h1 class="hero-title">LANTERN YARD FURNISHINGS</h1>
  <p class="hero-text">Lorem Ipsum is simply dummy text of the printing and typesetting industry. Lorem Ipsum has been the industry's standard dummy text ever since the 1500s.</p>
  <div class="btn" style="left:516px;top:394px;width:168px;height:41px">View products</div>
  <div class="dots" style="left:586px;top:612px"><i class="on"></i><i></i><i></i></div>
</header>

<section class="products">
  <h2 class="section-title" style="top:62px">PRODUCTS</h2>
  <div class="product" style="left:98px"><div class="product-photo" role="img" aria-label="TV enclosure product photo"></div><div class="product-meta"><span>Lorem ipsum is simply dummy</span><b>$700</b></div></div>
  <div class="product" style="left:449px"><div class="product-photo" role="img" aria-label="TV enclosure product photo"></div><div class="product-meta"><span>Lorem ipsum is simply dummy</span><b>$700</b></div></div>
  <div class="product" style="left:797px"><div class="product-photo" role="img" aria-label="TV enclosure product photo"></div><div class="product-meta"><span>Lorem ipsum is simply dummy</span><b>$700</b></div></div>
</section>

<section class="shipping">
  <p class="shipping-text">Free international shipping only 2 days 22:57:14</p>
  <div class="btn" style="left:958px;top:49px;width:141px;height:46px">Order now</div>
</section>

<section class="about">
  <h2 class="about-title">About company</h2>
  <p class="about-sub">Pellentesque interdum eget</p>
  <p class="about-text">Lorem Ipsum is simply dummy text of the printing and typesetting industry. Lorem Ipsum has been the industry's standard dummy text ever since the 1500s, when an unknown printer took a galley of type and scrambled it to make a type specimen book.</p>
  <div class="btn btn-outline" style="left:449px;top:196px;width:122px;height:38px;font-size:12px">Read more</div>
</section>

<section class="testimonial">
  <div class="abs" style="inset:0" role="img" aria-label="Photo of the entertainment cabinet with two televisions"></div>
  <div class="hero-shade"></div>
  <p class="quote">Hugely thought out!<br>Trying it now.I like the use of shape and background image!</p>
  <p class="quote-name">Mara Quill</p>
  <div class="dots" style="left:586px;top:250px"><i class="on"></i><i></i><i></i></div>
</section>

<section class="newsletter">
  <h2>STAY IN TOUCH</h2>
  <p>Sign Up for Email Updates on on News &amp; Offers</p>
  <div class="field" style="left:286px;top:161px;width:508px;border:none">Enter your email</div>
  <div class="btn" style="left:794px;top:161px;width:120px;height:41px;font-size:12px">Subscribe</div>
</section>

<section class="order">
  <h2 class="section-title" style="top:76px">ORDER FORM</h2>
  <div class="table-row table-head" style="top:140px;height:56px"><span style="left:0">Product</span><span style="left:313px">Unit cost</span><span style="left:626px">Quantity</span><span style="right:0">Total</span></div>
  <div class="table-row" style="top:196px"><span style="left:0">TV stand</span><span style="left:313px">$700</span><div class="qty">0 &nbsp;&nbsp;&nbsp;⌄</div><span style="right:0">$0</span></div>
  <div class="table-row" style="top:256px"><span style="left:0">TV stand <em>( Standard )</em></span><span style="left:313px">$800</span><div class="qty">0 &nbsp;&nbsp;&nbsp;⌄</div><span style="right:0">$0</span></div>
  <div class="table-row" style="top:316px"><span style="left:0">TV stand <em>( Premium )</em></span><span style="left:313px">$850</span><div class="qty">0 &nbsp;&nbsp;&nbsp;⌄</div><span style="right:0">$0</span></div>

  <p class="label" style="left:98px;top:452px">Payment method</p>
  <div class="field" style="left:98px;top:495px;width:231px">Card number</div>
  <div class="field" style="left:345px;top:495px;width:234px">Code</div>
  <div class="field select" style="left:98px;top:555px;width:231px">January</div>
  <div class="field select" style="left:345px;top:555px;width:234px">2014</div>
  <p class="label" style="left:98px;top:632px">Information</p>
  <div class="field" style="left:98px;top:675px;width:231px">First name</div>
  <div class="field" style="left:345px;top:675px;width:234px">Last name</div>
  <div class="field" style="left:98px;top:734px;width:481px">Your email</div>
  <p class="label" style="left:98px;top:810px">If you have coupon code</p>
  <div class="field" style="left:98px;top:846px;width:397px">Coupon code</div>
  <div class="btn" style="left:495px;top:846px;width:84px;height:41px;font-size:12px">Check</div>

  <p class="label" style="left:620px;top:452px">Delivery address</p>
  <div class="field" style="left:620px;top:495px;width:479px">Street address</div>
  <div class="field" style="left:620px;top:555px;width:479px">City</div>
  <div class="field" style="left:620px;top:615px;width:479px">Country</div>
  <div class="field" style="left:620px;top:675px;width:479px">Post code</div>
  <p class="label" style="left:620px;top:751px">Order summary</p>
  <div class="summary-row" style="top:786px;padding-bottom:10px;border-bottom:1px solid var(--line)"><span>Shipping cost:</span><span>Free</span></div>
  <div class="summary-row" style="top:830px;color:var(--ink)"><span>Total:</span><span>$0.00</span></div>
  <div class="btn" style="left:620px;top:871px;width:155px;height:41px;font-size:12px">Order product</div>
</section>

<section class="features">
  <div class="feature" style="left:172px">
    <svg width="52" height="60" viewBox="0 0 52 60" fill="none" stroke="#fff" stroke-width="3"><path d="M14 4h24v16a12 12 0 0 1-24 0z"/><path d="M14 9H5v5a9 9 0 0 0 9 9M38 9h9v5a9 9 0 0 1-9 9"/><path d="M26 32v12M16 56h20l-3-12H19z"/></svg>
    Quality guaranteed</div>
  <div class="feature" style="left:482px">
    <svg width="64" height="60" viewBox="0 0 64 60" fill="none" stroke="#fff" stroke-width="3"><rect x="4" y="12" width="34" height="30"/><path d="M38 22h12l10 12v8H38z"/><circle cx="16" cy="48" r="6" fill="#3cb6de"/><circle cx="50" cy="48" r="6" fill="#3cb6de"/><path d="M14 22l6 6 10-10"/></svg>
    Home delivery</div>
  <div class="feature" style="left:795px">
    <svg width="66" height="60" viewBox="0 0 66 60" fill="none" stroke="#fff" stroke-width="3"><rect x="3" y="14" width="46" height="32" rx="3"/><path d="M3 24h46M10 36h14"/><rect x="40" y="36" width="22" height="18" fill="#3cb6de"/><path d="M45 36v-6a6 6 0 0 1 12 0v6"/></svg>
    Secure payment</div>
</section>

<section class="contact">
  <h2 class="section-title" style="top:76px">CONTACT</h2>
  <p class="contact-sub">Do you have some kind of problem with our products?</p>
  <div class="contact-info">
    <strong>LANTERN YARD</strong>
    48 Birch Row, Fernvale<br>Country name : 908469
    <div class="line" style="margin-top:8px"><svg width="12" height="12" viewBox="0 0 12 12"><path d="M2 1h3l1 3-2 1a7 7 0 0 0 3 3l1-2 3 1v3c-6 0-9-3-9-9z" fill="var(--sky)"/></svg>(555) 014 - 2280</div>
    <div class="line"><svg width="12" height="10" viewBox="0 0 12 10"><rect width="12" height="10" fill="var(--sky)"/><path d="M0 0l6 5 6-5" stroke="#fff" fill="none"/></svg>hello@lanternyard.example</div>
  </div>
  <div class="field" style="left:528px;top:185px;width:465px">Your name</div>
  <div class="field" style="left:528px;top:242px;width:465px">Your email</div>
  <div class="field" style="left:528px;top:302px;width:465px;height:79px;align-items:flex-start;padding-top:12px">Your Message</div>
  <div class="btn" style="left:528px;top:394px;width:147px;height:44px;font-size:12px">Send message</div>
</section>

<footer class="footer">
  <p class="abs" style="left:98px;top:42px">© 2017. Lantern Yard. All rights reserved.</p>
  <p class="abs" style="left:734px;top:42px">Connect with our social network</p>
  <div class="social"><i></i><i></i><i></i><i></i><i></i></div>
</footer>

</body>
</html>
```